Aisle signage for supermarket

Design Isle signs for Indian supermarket. Modern, Clear, legible. Would be nice to use our logo colours. Signs Will be double sided and measure 900mm width x 400mm height. Indian theme would be nice. Attached files shows description to go on each sign.
Font styles to use
Sans Serif
Colors
Designer to choose colors to be used in the design.

```html
<!DOCTYPE html>
<html lang="en">
<head>
<meta charset="utf-8">
<title>Aisle Sign – Biscuits, Cakes, Tea, Coffee, Savouries</title>
<link href="https://fonts.googleapis.com/css2?family=Kanit:ital,wght@0,600;1,800&display=swap" rel="stylesheet">
<style>
  :root {
    --board-dark: #262626;
    --band-white: #ffffff;
    --green-deep: #2f6a3f;
    --green-mid: #4f8a44;
    --green-light: #7dae4b;
    --ink-white: #ffffff;
    --caption-ink: #1f1f1f;
    --brand-green: #2f6a3f;
  }
  html, body {
    margin: 0;
    padding: 0;
    overflow: hidden;
  }
  .board {
    position: relative;
    width: 1200px;
    height: 686px;
    background: var(--band-white);
    overflow: hidden;
    font-family: "Kanit", Arial, sans-serif;
  }
  .stage {
    position: absolute;
    left: 0;
    top: 0;
    width: 1200px;
    height: 560px;
    background: var(--board-dark);
  }
  .aisle-sign {
    position: absolute;
    left: 86px;
    top: 54px;
    width: 1029px;
    height: 459px;
    background: linear-gradient(100deg, var(--green-deep) 0%, var(--green-mid) 55%, var(--green-light) 100%);
    overflow: hidden;
  }
  .sign-pattern {
    position: absolute;
    inset: 0;
    background: radial-gradient(circle at 88% 68%, rgba(160, 205, 110, 0.28) 0%, rgba(160, 205, 110, 0.08) 38%, rgba(160, 205, 110, 0) 60%);
  }
  .sign-frame {
    position: absolute;
    left: 38px;
    top: 30px;
    width: 952px;
    height: 393px;
  }
  .sign-text {
    position: absolute;
    left: 77px;
    top: 0;
    margin: 0;
    color: var(--ink-white);
    font-weight: 800;
    font-style: italic;
    font-size: 84px;
    letter-spacing: 1px;
    text-transform: uppercase;
  }
  .sign-text span {
    position: absolute;
    left: 0;
    white-space: nowrap;
    line-height: 1;
  }
  .line-1 { top: 60px; }
  .line-2 { top: 180px; }
  .line-3 { top: 300px; }
  .caption {
    position: absolute;
    left: 30px;
    top: 595px;
    width: 560px;
    margin: 0;
    text-align: center;
    font-family: Arial, Helvetica, sans-serif;
    font-size: 21px;
    line-height: 23px;
    color: var(--caption-ink);
  }
  .brand-name {
    position: absolute;
    left: 776px;
    top: 596px;
    width: 385px;
    margin: 0;
    text-align: center;
    font-family: "Kanit", Arial, sans-serif;
    font-weight: 600;
    font-size: 40px;
    letter-spacing: 4px;
    color: var(--brand-green);
    line-height: 1.2;
  }
</style>
</head>
<body>
<main class="board">
  <section class="stage">
    <div class="aisle-sign">
      <div class="sign-pattern" role="img" aria-label="Faint Indian mandala pattern over the green background"></div>
      <svg class="sign-frame" viewBox="0 0 952 393" aria-hidden="true">
        <rect x="1.5" y="1.5" width="949" height="390" fill="none" stroke="#ffffff" stroke-width="3" stroke-dasharray="120 14 10 14"/>
      </svg>
      <h1 class="sign-text">
        <span class="line-1">Biscuits / Cakes</span>
        <span class="line-2">Tea / Coffe</span>
        <span class="line-3">Savouries</span>
      </h1>
    </div>
  </section>
  <p class="caption">11 supermarket aisle signs; fully vectorized material to ensure print quality.</p>
  <p class="brand-name">KESARI TRADERS</p>
</main>
</body>
</html>
```